TruvaLink Gastronomic Social Network

Truva Link is a Gastronomic Social Network that is focused on the relationship between restaurants and customers, creating new channels to communicate with themselves and developing new tools to modernize the classic menus. In Truva Link people will see images, videos and texts related on gastronomy shared by the bests restaurants of their cities in real time. Therefore the users will feel how easy is to choose a new restaurant only few minutes before leaving their homes and how useful is to choose a meal with the images of the digital menu in order to have the best experience possible.

Target Market(s)

The direct customers of the company are the restaurants, who pay monthly to post marketing content and their digital menu. The profile of the clients will not be too restrictive: from a restaurant that offers live music and drinks to a classic and expensive restaurant.

The final users of the product are families, couples, professionals and everyone who is interested in discovering new restaurants and good gastronomy.

Requirements
Must have
• We have the idea that after the splash screen show the last registered plates from the restaurants like in pictoria story. On the story we will show the plate for the current time like lunch or dinner, a logo of the restaurant, a small description and the price.
• When selected the plate the user will be redirected to a page will restaurant details showing the selected plate as first item on restaurant menu.
• For each plate we will have a page description showing ingredients, price, harmonization and button to reserve a table.
• Reserve a table is a page for reservation.
• Also we have a page for customer info, last selected plates and restaurants.

```html
<!DOCTYPE html>
<html lang="en">
<head>
<meta charset="utf-8">
<title>Story</title>
<link href="https://fonts.googleapis.com/css2?family=Roboto:wght@300;400;500;700&display=swap" rel="stylesheet">
<style>
  :root {
    --plum: #521f3e;
    --amber: #fba800;
    --white: #ffffff;
    --ink: #3a3a3a;
    --salmon: #d9774a;
    --salmon-deep: #a4472a;
  }
  * { margin: 0; padding: 0; box-sizing: border-box; }
  html, body { width: 675px; height: 1200px; overflow: hidden; background: var(--white); }
  body { font-family: 'Roboto', sans-serif; position: relative; }

  .app-bar {
    position: absolute; left: 0; top: 0; width: 675px; height: 99px;
    background: var(--plum);
  }
  .menu-button { position: absolute; left: 40px; top: 31px; width: 50px; height: 38px; }
  .menu-button span {
    position: absolute; left: 0; width: 50px; height: 3px; background: var(--white);
  }
  .menu-button span:nth-child(1) { top: 0; }
  .menu-button span:nth-child(2) { top: 17px; }
  .menu-button span:nth-child(3) { top: 34px; }
  .app-title {
    position: absolute; left: 0; right: 0; top: 22px; text-align: center;
    color: var(--white); font-weight: 300; font-size: 40px;
  }

  .dish-photo {
    position: absolute; left: 0; top: 99px; width: 675px; height: 827px;
    background:
      radial-gradient(ellipse at 40% 55%, rgba(110,140,50,0.35), transparent 45%),
      radial-gradient(ellipse at 55% 60%, var(--salmon) 0%, var(--salmon-deep) 55%, #3b1f16 100%);
  }
  .dish-photo::before {
    content: ""; position: absolute; inset: 0;
    background: linear-gradient(180deg, rgba(240,220,200,0.55) 0%, transparent 18%, transparent 80%, rgba(30,20,15,0.6) 100%);
  }

  .likes {
    position: absolute; left: 239px; top: 872px;
    color: var(--white); font-size: 28px; font-weight: 400;
  }
  .actions { position: absolute; left: 512px; top: 874px; display: flex; gap: 22px; }
  .actions svg { width: 30px; height: 30px; }

  .restaurant-badge {
    position: absolute; left: 32px; top: 832px; width: 190px; height: 190px;
    border-radius: 50%; background: var(--plum);
    display: flex; align-items: center; justify-content: center;
    color: var(--white); font-weight: 300; font-size: 36px;
  }

  .dish-name {
    position: absolute; left: 242px; top: 946px; width: 240px;
    color: var(--plum); font-weight: 500; font-size: 34px; line-height: 36px;
  }
  .rating { position: absolute; left: 512px; top: 953px; display: flex; gap: 4px; }
  .rating svg { width: 24px; height: 24px; }

  .dish-summary {
    position: absolute; left: 32px; top: 1051px; width: 385px;
    color: var(--ink); font-weight: 300; font-size: 29px; line-height: 36px;
  }
  .price-tag {
    position: absolute; left: 499px; top: 1057px; width: 145px; height: 63px;
    background: var(--amber); border-radius: 7px;
    display: flex; align-items: center; justify-content: center;
    color: var(--white); font-weight: 500; font-size: 33px;
  }
  .bottom-rule {
    position: absolute; left: 0; bottom: 0; width: 675px; height: 5px; background: var(--amber);
  }
</style>
</head>
<body>
  <header class="app-bar">
    <div class="menu-button"><span></span><span></span><span></span></div>
    <h1 class="app-title">Story</h1>
  </header>

  <div class="dish-photo" role="img" aria-label="Close-up of seared salmon fillets topped with sesame seeds and chopped scallions, chopsticks in the background"></div>

  <div class="likes">34 likes</div>
  <div class="actions">
    <svg viewBox="0 0 30 30" fill="none" stroke="#fff" stroke-width="2" stroke-linejoin="round"><path d="M15 26 C4 18 2 13 3.5 8.5 C5 4.5 11 3.5 15 9 C19 3.5 25 4.5 26.5 8.5 C28 13 26 18 15 26 Z"/></svg>
    <svg viewBox="0 0 30 30" fill="none" stroke="#fff" stroke-width="2" stroke-linejoin="round"><path d="M15 3 A12 12 0 1 0 24 23 L27 27 L26 20 A12 12 0 0 0 15 3 Z"/></svg>
    <svg viewBox="0 0 30 30" fill="none" stroke="#fff" stroke-width="2" stroke-linejoin="round"><path d="M3 4 L28 4 L14 27 L12 15 Z M12 15 L28 4"/></svg>
  </div>

  <div class="restaurant-badge">LOGO</div>

  <h2 class="dish-name">Lorem Ipsum Dolor</h2>
  <div class="rating" aria-label="4 of 5 stars">
    <svg viewBox="0 0 24 24"><path fill="#fba800" d="M12 2 L14.9 8.6 L22 9.3 L16.6 14 L18.2 21 L12 17.3 L5.8 21 L7.4 14 L2 9.3 L9.1 8.6 Z"/></svg>
    <svg viewBox="0 0 24 24"><path fill="#fba800" d="M12 2 L14.9 8.6 L22 9.3 L16.6 14 L18.2 21 L12 17.3 L5.8 21 L7.4 14 L2 9.3 L9.1 8.6 Z"/></svg>
    <svg viewBox="0 0 24 24"><path fill="#fba800" d="M12 2 L14.9 8.6 L22 9.3 L16.6 14 L18.2 21 L12 17.3 L5.8 21 L7.4 14 L2 9.3 L9.1 8.6 Z"/></svg>
    <svg viewBox="0 0 24 24"><path fill="#fba800" d="M12 2 L14.9 8.6 L22 9.3 L16.6 14 L18.2 21 L12 17.3 L5.8 21 L7.4 14 L2 9.3 L9.1 8.6 Z"/></svg>
    <svg viewBox="0 0 24 24"><path fill="none" stroke="#fba800" stroke-width="1.5" d="M12 2 L14.9 8.6 L22 9.3 L16.6 14 L18.2 21 L12 17.3 L5.8 21 L7.4 14 L2 9.3 L9.1 8.6 Z"/></svg>
  </div>

  <p class="dish-summary">Lorem ipsum dolor sit amet, consectetur adipisicing elit, sed do eiusmod tempor.</p>
  <div class="price-tag">$ 24</div>

  <div class="bottom-rule"></div>
</body>
</html>
```